Pulse Arena's Website Redesign.

Pulse Arena is an Indoor Laser Tag chain that is based in Malaysia.
We would like to revamp our current design.

Current website is www.glowzonetag.com.my

More pictures can be found in our facebook
www.facebook.com/glowzonetag
www.facebook.com/pulsearenajohor

You can use whatever pictures and materials found in current website and facebook for the proposal. More graphics can be provided later on when we are satisfied with the design. Please feel free to ask more questions.

Website should have:

1. A contact form.
2. Interface to display twitter updates.
3. Links to facebook.
4. Content management system
5. Integration to Google Maps to show location of branches.

Devon

Target Market(s)

13 years old to 35 years old.
Corporates.

Font styles to use
Serif
Sans Serif

Colors
eb1f27
0255a3

Requirements
Must have
• 1. A contact form.
• 2. Interface to display twitter updates.
• 3. Links to facebook.
• 4. Content management system
• 5. Integration to Google Maps to show location of branches.
Nice to have
• Open to suggestions

```html
<!DOCTYPE html>
<html lang="en">
<head>
<meta charset="utf-8">
<title>Pulse Arena – Indoor Laser Tag</title>
<link href="https://fonts.googleapis.com/css2?family=Arimo:wght@400;700&display=swap" rel="stylesheet">
<style>
:root{
  --red:#eb1f27;
  --blue:#0255a3;
  --page:#1b3f9e;
  --navy:#0a1f5c;
  --deep:#061236;
  --panel:#0d2a73;
  --sky:#4fa8ff;
  --white:#ffffff;
  --ink:#333;
  --muted:#9fb4e0;
}
*{box-sizing:border-box;margin:0;padding:0}
html,body{width:672px;height:1200px;overflow:hidden}
body{position:relative;background:var(--page);font-family:"Arimo",Arial,sans-serif;color:var(--white);font-size:7px;line-height:1.35}
.abs{position:absolute}

/* header */
.site-header{left:0;top:0;width:672px;height:59px;background:linear-gradient(#0f2f86,#061a55)}
.brand{left:276px;top:4px;width:120px;height:50px;background:linear-gradient(#ffffff,#d7e3f5);border-radius:0 0 10px 10px;display:flex;align-items:center;justify-content:center;gap:5px}
.brand-dot{width:10px;height:10px;border-radius:50%;background:var(--blue)}
.brand-name{color:var(--blue);font-weight:700;font-size:14px}
.phone{left:448px;top:14px;font-size:17px;font-weight:700;display:flex;align-items:center;gap:6px;white-space:nowrap}
.main-nav{left:0;top:59px;width:672px;height:23px;background:linear-gradient(#1a4bc0,#0b2d86);border-top:1px solid #3d6fe0}
.main-nav ul{list-style:none;display:flex;margin-left:92px;height:100%}
.main-nav li{padding:0 8px;font-size:7.5px;display:flex;align-items:center;border-right:1px solid #3d6fe0}

/* hero */
.hero{left:0;top:82px;width:672px;height:200px;background:linear-gradient(120deg,#3a2a4a,#6a3f4a 40%,#2c2f4f 70%,#1e2440)}
.hero-arrow{top:85px;width:14px;height:28px;background:rgba(0,0,0,.4);display:flex;align-items:center;justify-content:center;font-size:12px}
.hero-title{left:0;width:672px;top:125px;text-align:center;font-size:14px;font-weight:700;text-transform:uppercase}
.hero-sub{left:186px;width:300px;top:148px;text-align:center;font-size:8px}
.dots{left:0;width:672px;top:191px;display:flex;justify-content:center;gap:4px}
.dots span{width:6px;height:6px;border-radius:50%;background:#aaa}
.dots span.on{background:var(--red)}

/* features */
.features{left:92px;top:290px;width:488px;height:122px;background:linear-gradient(#2c5ac7,#163d99);border-radius:8px;display:flex;gap:6px;padding:10px 8px}
.feature{flex:1;background:var(--deep);border-radius:4px;position:relative}
.feature h3{height:19px;background:linear-gradient(#3d7fe6,#1b4fb5);text-align:center;font-size:10px;font-weight:400;line-height:19px}
.feature .icon{left:10px;top:30px;width:36px;height:36px}
.feature p{position:absolute;left:55px;top:30px;width:95px;font-size:7px}
.more{right:6px;bottom:6px;background:linear-gradient(#2e6bd6,#143f9a);border-radius:8px;padding:2px 8px;font-size:6px}

/* content */
.content{left:96px;top:418px;width:320px;height:542px;background:var(--white);border-radius:8px;color:var(--ink);padding:12px 18px}
.content h1{font-size:11px;margin-bottom:8px;color:#111}
.content h1 span{color:var(--red)}
.content p{font-size:6.4px;margin-bottom:7px;color:#444}
.team-photo{left:25px;top:214px;width:270px;height:148px;background:linear-gradient(135deg,#2a3c8a,#6b4a70 50%,#2a2d4f)}
.gallery-title{left:18px;top:388px;font-size:11px;font-weight:700;color:#222}
.thumbs{left:25px;top:410px;width:270px;display:grid;grid-template-columns:repeat(4,58px);gap:13px 12px}
.thumbs div{height:42px;background:linear-gradient(135deg,#203880,#7a3a66);border:2px solid #ddd}
.view-all{right:22px;bottom:10px;font-size:6px;color:var(--blue)}

/* sidebar */
.side{left:424px;width:156px;background:var(--navy);border:1px solid #2d5bc4}
.side h4{height:17px;background:linear-gradient(#3a7ae0,#1a4cb2);font-size:7.5px;font-weight:400;line-height:17px;padding-left:8px;text-transform:uppercase}
.tweet{padding:4px 8px;font-size:5.8px;color:var(--muted);border-bottom:1px solid #223f8e}
.tweet em{font-style:normal;color:var(--sky);float:right}
.blog-title{padding:6px 8px;font-size:8px;font-weight:700}
.blog-date{padding:0 8px;font-size:5.5px;color:var(--muted)}
.blog-photo{left:8px;top:68px;width:58px;height:56px;background:linear-gradient(#304b8f,#1b2a55)}
.blog-text{left:72px;top:68px;width:78px;font-size:5.8px;color:var(--muted)}
.btn{background:linear-gradient(#3a7ae0,#1a4cb2);font-size:6px;padding:3px 8px}
.news{display:flex;gap:6px;padding:8px 8px 7px;font-size:5.5px}
.news .thumb{width:26px;height:25px;flex:none;background:linear-gradient(135deg,#3cae5a,#e0b33a)}
.news b{color:var(--sky);font-weight:400;display:block}

/* testimonials */
.reviews{left:96px;top:967px;width:484px;height:89px;background:var(--panel);border-top:1px solid #2d5bc4}
.reviews h4{left:10px;top:6px;font-size:8px;font-weight:400;color:#ddd}
.review{top:24px;width:150px;display:flex;gap:6px}
.avatar{width:26px;height:26px;border-radius:50%;background:linear-gradient(#cfd6e6,#8a94ab);flex:none;border:2px solid #ccc}
.review p{font-size:6px}
.who{top:60px;font-size:6px;color:#ddd}
.pager{right:8px;top:70px;font-size:8px}

/* footer */
.site-footer{left:0;top:1056px;width:672px;height:116px;background:var(--deep)}
.col{top:8px;font-size:6.2px;color:#cfd8ee}
.col h5{font-size:7.5px;color:var(--white);margin-bottom:4px}
.social{display:flex;gap:3px;margin-top:3px}
.social span{width:10px;height:10px;background:#2f6fd0}
.newsletter{left:426px;top:40px;width:155px;height:66px;background:linear-gradient(#1c4fb8,#0e2c78);border-radius:4px;padding:4px 6px}
.newsletter h6{font-size:6.5px;font-weight:400;background:var(--blue);display:inline-block;padding:1px 4px;margin-bottom:4px}
.newsletter .lead{margin-left:26px;font-size:6px;margin-bottom:3px}
.newsletter .field{margin-left:26px;height:11px;background:var(--white);color:#888;font-size:5.5px;padding:2px 3px}
.newsletter .submit{margin:4px 0 0 68px;width:50px;height:12px;background:#111;border:1px solid #444;font-size:6.5px;font-weight:700;text-align:center;line-height:11px}
.envelope{left:7px;top:20px;width:20px;height:16px}
.copyright{left:0;top:1172px;width:672px;height:28px;background:#02081f;text-align:center;line-height:28px;font-size:6.5px;color:#ccc}
</style>
</head>
<body>

<header class="site-header abs">
  <div class="brand abs"><span class="brand-dot"></span><span class="brand-name">Pulse Arena</span></div>
  <div class="phone abs">
    <svg width="16" height="16" viewBox="0 0 24 24"><path fill="#4fa8ff" d="M6.6 10.8a15 15 0 0 0 6.6 6.6l2.2-2.2a1 1 0 0 1 1-.25 11.4 11.4 0 0 0 3.6.57 1 1 0 0 1 1 1V20a1 1 0 0 1-1 1A17 17 0 0 1 3 4a1 1 0 0 1 1-1h3.5a1 1 0 0 1 1 1c0 1.25.2 2.45.57 3.57a1 1 0 0 1-.25 1z"/></svg>
    888 - 2468 - 1357
  </div>
</header>

<nav class="main-nav abs">
  <ul>
    <li>HOME</li><li>PHOTO GALLERY</li><li>FAQ'S</li><li>CONTACT US</li><li>OUTDOOR LASER TAG</li><li>COMPARISON OF FEATURES</li><li>ONLINE BOOKING</li>
  </ul>
</nav>

<section class="hero abs" role="img" aria-label="Group of laser tag players in glowing vests holding blasters in the arena">
  <div class="hero-arrow abs" style="left:4px">‹</div>
  <div class="hero-arrow abs" style="right:4px">›</div>
  <h2 class="hero-title abs">Lorem ipsum dolor sit amet, consecteteur adipiscing elit</h2>
  <p class="hero-sub abs">Lorem ipsum dolor sit amet, consectetuer adipiscing elit. sed diem nonumy inconvalis gravida neque, lorem ipsum dolor sit amet.</p>
  <div class="dots abs"><span></span><span class="on"></span><span></span><span></span></div>
</section>

<section class="features abs">
  <article class="feature">
    <h3>WHO WE ARE</h3>
    <svg class="icon abs" viewBox="0 0 36 36"><g fill="#4fa8ff"><circle cx="12" cy="10" r="5"/><path d="M3 30c0-8 4-12 9-12s9 4 9 12z"/><circle cx="25" cy="12" r="4"/><path d="M18 30c0-7 3-10 7-10s8 3 8 10z"/></g></svg>
    <p>Lorem ipsum dolor sit amet, consectetuer adipiscing elit. Sed diem nonumy...</p>
    <span class="more abs">▸ Read more</span>
  </article>
  <article class="feature">
    <h3>WHAT WE DO</h3>
    <svg class="icon abs" viewBox="0 0 36 36"><g fill="#4fa8ff"><circle cx="12" cy="9" r="5"/><path d="M4 32c0-9 3-14 8-14s8 5 8 14z"/><rect x="20" y="16" width="13" height="10"/><rect x="18" y="26" width="17" height="3"/></g></svg>
    <p>Lorem ipsum dolor sit amet, consectetuer adipiscing elit. Sed diem nonumy...</p>
    <span class="more abs">▸ Read more</span>
  </article>
  <article class="feature">
    <h3>OUR BUSINESS</h3>
    <svg class="icon abs" viewBox="0 0 36 36"><path fill="#4fa8ff" d="M2 14l8-4 6 3 6-3 12 5-4 8-10 6-6-4-8-2z"/></svg>
    <p>Lorem ipsum dolor sit amet, consectetuer adipiscing elit. Sed diem nonumy...</p>
    <span class="more abs">▸ Read more</span>
  </article>
</section>

<main class="content abs">
  <h1>Welcome to <span>Pulsearenatag.com.my</span></h1>
  <p>Lorem ipsum dolor sit amet, consectetuer adipiscing elit, sed diem nonumy in convallis gravida neque. Nulla gravida vestibulum mattis a accumsan, aliquam in sagittis at. Sollicitudin sed massa ut enim veniam. Curabitur tempus sem vitae mi vestibulum volutpat malesuada erat vestibulum. Sed aliquam dolor at dolor consec quat gravida. Fusce minesque tempus nec feugiat sit amet. Tincidunt ut leo. Nam semper ornare enim.</p>
  <p>Lorem ipsum dolor sit amet, consectetuer adipiscing elit, sed diem nonumy inconvalis gravida neque. Nulla gravida vestibulum mattis a accumsan, aliquam in sagittis at. Sollicitudin sed massa ut enim veniam. Curabitur tempus sem vitae mi vestibulum volutpat malesuada erat vestibulum. Sed aliquam dolor at dolor consequat gravida. Fusce minesque tempus nec feugiat sit amet. Tincidunt ut leo. Nam semper ornare enim.</p>
  <p>Lorem ipsum dolor sit amet, consectetuer adipiscing elit, sed diem nonumy in convallis gravida neque. Nulla gravida vestibulum mattis a accumsan, aliquam in sagittis at. Curabitur tempus sem vitae mi vestibulum volutpat malesuada erat vestibulum, sed ut quam dolor at dolor consequat gravida. Fusce minesque nec feugiat sit amet. Tincidunt ut leo. Nam semper ornare enim.</p>
  <p>Lorem ipsum dolor sit amet, consectetuer adipiscing elit. Sed diem nonumy inconvalis gravida neque. nulla gravida vestibulum mattis a accumsan, aliquam in sagittis ut. sollicitudin sed massa ut nim veniam.</p>
  <div class="team-photo abs" role="img" aria-label="Team of laser tag players posing together in the arena"></div>
  <h2 class="gallery-title abs">Gallery Photos</h2>
  <div class="thumbs abs" role="img" aria-label="Eight gallery photos of laser tag games">
    <div></div><div></div><div></div><div></div><div></div><div></div><div></div><div></div>
  </div>
  <span class="view-all abs">View all</span>
</main>

<aside class="side abs" style="top:424px;height:112px">
  <h4>Live Feed</h4>
  <div class="tweet">facilisis felis dolor@tempus eget lobortis id libero Donec scelerisque leo ac risus. <em>2 hours ago</em></div>
  <div class="tweet">facilisis felis dolor@tempus eget lobortis id libero Donec scelerisque leo ac risus. <em>3 hours ago</em></div>
  <div class="tweet" style="border:0">facilisis felis dolor@tempus eget lobortis id libero Donec scelerisque leo ac risus. <em>4 hours ago</em></div>
</aside>

<aside class="side abs" style="top:544px;height:217px">
  <h4>Recent Blog Posts</h4>
  <div class="blog-title">Lorem ipsum dolor sit amet, consectetuer</div>
  <div class="blog-date">July, 5th, 2014</div>
  <div class="blog-photo abs" role="img" aria-label="Player in a laser tag vest"></div>
  <p class="blog-text abs">Lorem ipsum dolor sit amet, consectetuer adipiscing elit, sed diem nonumy in convallis gravida neque. Nulla gravida vestibulum mattis a accumsan, aliquam in sagittis at. Curabitur tempus sem vitae mi vestibulum volutpat.</p>
  <span class="btn abs" style="left:0;top:160px">MORE POSTS</span>
  <span class="abs" style="right:8px;top:163px;font-size:6px">read more</span>
</aside>

<aside class="side abs" style="top:771px;height:172px">
  <h4>Latest News &amp; Events</h4>
  <div class="news"><div class="thumb"></div><div><b>Lorem ipsum dolor sit amet, Cons ectetuer adipiscing elit.</b>January, 13th, 2014</div></div>
  <div class="news"><div class="thumb"></div><div><b>Lorem ipsum dolor sit amet, Cons ectetuer adipiscing elit.</b>January, 13th, 2014</div></div>
  <div class="news"><div class="thumb"></div><div><b>Lorem ipsum dolor sit amet, Cons ectetuer adipiscing elit.</b>January, 13th, 2014</div></div>
  <div class="news"><div class="thumb"></div><div><b>Lorem ipsum dolor sit amet, Cons ectetuer adipiscing elit.</b>January, 13th, 2014</div></div>
  <span class="abs" style="right:8px;bottom:5px;font-size:6px">View All</span>
</aside>

<section class="reviews abs">
  <h4 class="abs">What Customers Say</h4>
  <div class="review abs" style="left:14px"><span class="avatar"></span><p>"Lorem ipsum dolor sit amet, consectetuer adipiscing elit. Sed diem nonumy inconvalis gravida neque."</p></div>
  <div class="who abs" style="left:46px">Kevin Lim, Perak</div>
  <div class="review abs" style="left:172px"><span class="avatar"></span><p>"Lorem ipsum dolor sit amet, consectetuer adipiscing elit. Sed diem nonumy inconvalis gravida neque."</p></div>
  <div class="who abs" style="left:204px">Aidil Rahman, Kualalumpur</div>
  <div class="review abs" style="left:330px"><span class="avatar"></span><p>"Lorem ipsum dolor sit amet, consectetuer adipiscing elit. Sed diem nonumy inconvalis gravida neque."</p></div>
  <div class="who abs" style="left:362px">Marcus Tan, Pahang</div>
  <span class="pager abs">‹ ›</span>
</section>

<footer class="site-footer abs">
  <div class="col abs" style="left:100px">
    <h5>Get In Touch</h5>
    Pulse Arena, Bhd<br><br>Address :<br>Lorem Ipsum, 1258543,<br>Lorem, Kualalumpur, ZIP code<br><br>Phone : XXX - XXXX - XXX<br>Fax : XXX - XXXX - XXXX<br>email : info@pulsearenatag.com.my
  </div>
  <div class="col abs" style="left:228px">
    <h5>Main menu</h5>
    Home<br>Photo Gallery<br>FAQ's<br>Contact Us<br>Outdoorlasertag<br>Comparison of features<br>Online Booking<br>Blog<br>Testimonials
  </div>
  <div class="col abs" style="left:322px">
    <h5>Usefull Links</h5>
    Sitemap<br>Terms &amp; Conditions<br>Privacy Policy<br>Help<br>Latest News &amp; Updates<br>Recent Blog Posts<br>Newsletter<br><br>Follow us on
    <div class="social"><span></span><span></span><span></span></div>
  </div>
  <div class="col abs" style="left:428px"><h5>CONTACT US</h5></div>
  <div class="newsletter abs">
    <h6>NEWSLETTER</h6>
    <svg class="envelope abs" viewBox="0 0 20 16"><rect x="1" y="2" width="18" height="12" fill="#fff"/><path d="M1 2l9 7 9-7" fill="none" stroke="#0255a3" stroke-width="1.2"/></svg>
    <div class="lead">Receiving our new look monthly</div>
    <div class="field">Enter your email address</div>
    <div class="submit">SUBMIT</div>
  </div>
</footer>

<div class="copyright abs">Copyright © 2014, www.glowzonetag.com.my All rights reserved.</div>

</body>
</html>
```